Business cards for Marrowfield Consulting with the following info for the front side:

Marrowfield Consulting
Executive Coaching and Human Capital Strategy
www.marrowfield.example

Idalia Renvoort
Principal
idalia@marrowfield.example
+1 555 274 9186

Black background, text using the colours of the logo - enclosed.

The back side of the business card should feature the logo in the middle, with "Executive Coaching and Human Capital Strategy" on top and "www.marrowfield.example" below.

```html
<!DOCTYPE html>
<html lang="en">
<head>
<meta charset="utf-8">
<title>Marrowfield Consulting – Business Cards</title>
<link href="https://fonts.googleapis.com/css2?family=Roboto:wght@300;400;500;700&display=swap" rel="stylesheet">
<style>
  :root {
    --backdrop: #e9e9e9;
    --card-black: #1e1d1d;
    --brand-blue: #2a9fd6;
    --brand-yellow: #f2c01c;
    --emboss-grey: #3a3a3a;
    --edge-yellow: #f5c518;
  }
  * { box-sizing: border-box; margin: 0; padding: 0; }
  html, body {
    width: 1200px; height: 801px; overflow: hidden;
    background: var(--backdrop);
    font-family: "Roboto", Arial, sans-serif;
  }
  .sheet {
    position: relative; width: 1200px; height: 801px;
    display: flex; align-items: center; justify-content: center; gap: 60px;
  }
  .card {
    position: relative; width: 525px; height: 300px;
    background: var(--card-black);
    border-bottom: 3px solid var(--edge-yellow);
    border-right: 3px solid var(--edge-yellow);
    box-shadow: 0 10px 24px rgba(0,0,0,0.22);
  }

  /* Front */
  .card-front .brand {
    position: absolute; left: 34px; top: 130px;
    display: flex; align-items: center; gap: 10px;
  }
  .brand-dot {
    width: 34px; height: 34px; border-radius: 50%;
    border: 2px solid var(--brand-blue);
  }
  .brand-name {
    font-weight: 500; font-size: 25px; letter-spacing: 1px;
    color: var(--brand-blue); text-transform: uppercase;
  }
  .divider {
    position: absolute; left: 262px; top: 88px;
    width: 1px; height: 124px; background: var(--brand-blue);
  }
  .contact {
    position: absolute; left: 290px; top: 84px;
  }
  .contact-name {
    font-weight: 700; font-size: 20px; color: var(--brand-yellow);
  }
  .contact-role {
    font-weight: 300; font-size: 14px; color: var(--brand-blue);
    margin: 2px 0 12px;
  }
  .contact-list { list-style: none; }
  .contact-list li {
    display: flex; align-items: center; gap: 9px;
    font-weight: 300; font-size: 14px; color: var(--brand-blue);
    line-height: 22px;
  }
  .contact-list svg { width: 12px; height: 12px; fill: var(--brand-yellow); flex: none; }

  /* Back */
  .card-back { text-align: center; }
  .tagline {
    position: absolute; left: 0; right: 0; top: 58px;
    font-weight: 300; font-size: 16px; color: var(--brand-yellow);
  }
  .card-back .brand {
    position: absolute; left: 0; right: 0; top: 118px;
    display: flex; align-items: center; justify-content: center; gap: 14px;
  }
  .card-back .brand-dot {
    width: 50px; height: 50px; border-color: var(--emboss-grey);
  }
  .card-back .brand-name {
    font-size: 38px; color: var(--emboss-grey); letter-spacing: 1.5px;
  }
  .back-url {
    position: absolute; left: 0; right: 0; top: 222px;
    font-weight: 300; font-size: 16px; color: var(--brand-blue);
  }
</style>
</head>
<body>
<main class="sheet">
  <section class="card card-front" aria-label="Card front">
    <div class="brand">
      <span class="brand-dot"></span>
      <span class="brand-name">Marrowfield</span>
    </div>
    <div class="divider"></div>
    <div class="contact">
      <p class="contact-name">Idalia Renvoort</p>
      <p class="contact-role">Principal</p>
      <ul class="contact-list">
        <li>
          <svg viewBox="0 0 24 24" aria-hidden="true"><path d="M6.6 10.8a15.1 15.1 0 0 0 6.6 6.6l2.2-2.2c.3-.3.7-.4 1-.2 1.1.4 2.3.6 3.6.6.6 0 1 .4 1 1V20c0 .6-.4 1-1 1A17 17 0 0 1 3 4c0-.6.4-1 1-1h3.5c.6 0 1 .4 1 1 0 1.3.2 2.5.6 3.6.1.3 0 .7-.2 1z"/></svg>
          +1 555 274 9186
        </li>
        <li>
          <svg viewBox="0 0 24 24" aria-hidden="true"><path d="M2 5h20v14H2z M3.5 6.5 12 13l8.5-6.5" fill="none" stroke="#f2c01c" stroke-width="2.4"/></svg>
          idalia@marrowfield.example
        </li>
        <li>
          <svg viewBox="0 0 24 24" aria-hidden="true"><circle cx="12" cy="12" r="10"/><path d="M2 12h20M12 2c3 3 3 17 0 20M12 2c-3 3-3 17 0 20" fill="none" stroke="#1e1d1d" stroke-width="1.6"/></svg>
          www.marrowfield.example
        </li>
      </ul>
    </div>
  </section>

  <section class="card card-back" aria-label="Card back">
    <p class="tagline">Executive Coaching and Human Capital Strategy</p>
    <div class="brand">
      <span class="brand-dot"></span>
      <span class="brand-name">Marrowfield</span>
    </div>
    <p class="back-url">www.marrowfield.example</p>
  </section>
</main>
</body>
</html>
```